Billboard design 8x3M NURA (Spanish company)

We´re located in the south of Spain. We run a local telecom company.
We sell Fiber optic, and mobile phone lines mainly.
The billboard will have to be in Spanish, I would like the price to be something you spot on first sight when passing by in the car.
Our company color is blue, like in our logo which I will add. I will also add a example from what we currently have.
The new offer should be:
1000 megas + 100Gigas movil con llamadas ilimitadas. (meaning 1000Mb fiber optic speed and 100Gb data and unlimited calls for 1 mobile line)
Our details are: phone line 952 00 0147
Website: nu-ra.es

```html
<!DOCTYPE html>
<html lang="es">
<head>
<meta charset="utf-8">
<title>NURA – Valla 8x3</title>
<link rel="stylesheet" href="https://fonts.googleapis.com/css2?family=Montserrat:wght@500;600;700;800&display=swap">
<style>
  :root {
    --page-bg: #e9edf0;
    --board-top: #3b7c9c;
    --board-bottom: #1f5574;
    --navy: #15364d;
    --white: #ffffff;
    --gold: #d9a21f;
    --visual-cool: rgba(214, 228, 236, 0.22);
    --visual-warm: rgba(232, 150, 96, 0.30);
  }
  * { box-sizing: border-box; margin: 0; padding: 0; }
  html, body {
    width: 1200px; height: 1200px; overflow: hidden;
    background: var(--page-bg);
    font-family: "Montserrat", Arial, sans-serif;
  }
  .billboard {
    position: absolute; left: 40px; top: 390px;
    width: 1120px; height: 420px;
    background: linear-gradient(160deg, var(--board-top) 0%, #2d6a8b 45%, var(--board-bottom) 100%);
    overflow: hidden;
  }
  .fiber-visual {
    position: absolute; left: 340px; top: 50px; width: 320px; height: 300px;
    background: linear-gradient(90deg, var(--visual-cool) 0%, var(--visual-warm) 100%);
  }
  .brand { position: absolute; left: 50px; top: 72px; color: var(--white); }
  .brand-name { font-size: 66px; font-weight: 800; letter-spacing: 2px; line-height: 1; }
  .brand-services { font-size: 17px; font-weight: 600; margin-top: 6px; }
  .headline {
    position: absolute; left: 50px; top: 192px;
    color: var(--white); font-size: 25px; font-weight: 700; line-height: 1.3;
    text-transform: uppercase;
  }
  .accent-bar {
    position: absolute; left: 50px; top: 270px; width: 240px; height: 14px;
    border-radius: 7px; background: var(--gold);
  }
  .contact { position: absolute; left: 50px; top: 298px; color: var(--white); font-weight: 700; font-size: 29px; line-height: 1.4; }
  .contact-phone { display: flex; align-items: center; gap: 10px; }
  .contact-phone svg { width: 16px; height: 26px; }
  .legal {
    position: absolute; left: 450px; top: 372px;
    color: var(--white); font-size: 12px; font-weight: 600;
  }
  .price-box {
    position: absolute; left: 700px; top: 64px; width: 360px; height: 112px;
    background: var(--navy); border-radius: 18px;
    color: var(--white); font-weight: 800; font-size: 88px; line-height: 112px;
    text-align: center; letter-spacing: -1px;
  }
  .price-box .unit { font-size: 50px; letter-spacing: 0; }
  .data {
    position: absolute; left: 690px; top: 184px;
    color: var(--navy); font-size: 66px; font-weight: 800; line-height: 1;
  }
  .mobile {
    position: absolute; left: 690px; top: 260px;
    display: flex; align-items: center; gap: 12px;
    color: var(--navy); font-size: 76px; font-weight: 800; line-height: 1;
  }
  .mobile svg { width: 30px; height: 60px; }
  .calls {
    position: absolute; left: 690px; top: 342px;
    color: var(--navy); font-size: 24px; font-weight: 700; line-height: 1.25;
  }
</style>
</head>
<body>
  <section class="billboard">
    <div class="fiber-visual" role="img" aria-label="Fotografía de un haz de fibra óptica luminoso"></div>

    <div class="brand">
      <div class="brand-name">NURA</div>
      <div class="brand-services">Wifi | Fibra | Movil | Tv</div>
    </div>

    <p class="headline">Tu fibra + móvil<br>al mejor precio</p>
    <div class="accent-bar"></div>

    <div class="contact">
      <div class="contact-phone">
        <svg viewBox="0 0 16 26" aria-hidden="true"><rect x="1.5" y="1.5" width="13" height="23" rx="3" fill="none" stroke="#fff" stroke-width="2.5"/></svg>
        952 00 0147
      </div>
      <div class="contact-web">www.nu-ra.es</div>
    </div>

    <p class="legal">*Consulte condiciones</p>

    <div class="price-box">1000<span class="unit">mb</span></div>
    <div class="data">+ 100 Gb</div>
    <div class="mobile">
      <svg viewBox="0 0 30 60" aria-hidden="true"><rect x="3" y="3" width="24" height="54" rx="6" fill="none" stroke="#15364d" stroke-width="4"/><line x1="11" y1="49" x2="19" y2="49" stroke="#15364d" stroke-width="3" stroke-linecap="round"/></svg>
      móvil
    </div>
    <p class="calls">con llamadas<br>ilimitadas</p>
  </section>
</body>
</html>
```